Pactwise - Training I Consulting I Review - Related to Contracts/Agreements

We provide legal services, we need a plattform to book video online trainings or local trainings classes and appointments (with calendar feature to select date and see availability at screen), payment over internet, legal document creation over webpage, videos will be produces in the next 3 - 4 moths so this is a place holder item. Participants for the Online trainings shall have a login in area with secured password. Appointments for local trainings and Consulting. Consider Outline in file attached. I can send you also a video with more explanation regarding the purpose.

Target Market(s)

Startup/scale up Software companies that intent to have an international business and need help with their contracts, to sell their products. Sales persons.

Industry/Entity Type

Legal

Coding

Coded - Design and coding required

Number of Pages Required

5+ page

Font styles to use
Serif
Sans Serif

Colors
000000
eeeeee
f5f5f5
ffffff
f8fcfd
3277b5
ecf7fb
cadf82
86cfc6

Requirements
Must have
• See file pactwise attached with outline. Moreover see here first starting point: https://moritz-ebbing.sitebuildr-demo.net/mysite-1 . Main inspiration comes from www.advisoryhub-demo.net from the log in area, see the outline in the file attached with the screen shots. At the end I need someone who can draft the full webpage and maintain it for a yearly fee. It must be simple and well structured layout. Lean. 1st landing page shall not scroll, 2 landing page only a little to see the testimonials and foster of page. There should be a Progress Bar to indicate the booking/selection process. Calendar booking. Easy fast booking.
• I like the colour mix, the feeling and the easy structor of:
• https://www.artpitch-demo.net/design/6374387or
• https://www.artpitch-demo.net/design/6372391 or https://www.artpitch-demo.net/design/6374366
• https://www.agencyfind-demo.net/en/web-design/belgium-be
• https://www.artpitch-demo.net/design/5896857
• https://www.artpitch-demo.net/design/5902173
• https://www.artpitch-demo.net/design/17197349
• https://www.artpitch-demo.net/design/5464461
• https://www.artpitch-demo.net/design/7180908
Nice to have
• page for evaluation and interview, see outline attached in the file with screen shots. Document upload.
Should not have
• many pictures, long scroll down pages on the 1st and 2nd ladding pages, many colours and forms. No need for news letter, search field, no need for links to Chatterly and other social media (except workNet).

```html
<!DOCTYPE html>
<html lang="en">
<head>
<meta charset="utf-8">
<title>Pactwise – Contracts</title>
<link rel="stylesheet" href="https://fonts.googleapis.com/css2?family=Playfair+Display:wght@400&family=Libre+Baskerville&family=Open+Sans:wght@700&display=swap">
<style>
  :root {
    --white: #ffffff;
    --accent-red: #ec1c24;
    --shade-dark: #2c2c30;
    --shade-mid: #45434a;
    --shade-warm: #6a5a52;
    --shade-left: #5b5048;
  }
  * { margin: 0; padding: 0; box-sizing: border-box; }
  html, body {
    width: 1200px;
    height: 632px;
    overflow: hidden;
    background: var(--shade-dark);
  }
  .landing {
    position: relative;
    width: 1200px;
    height: 632px;
    overflow: hidden;
    color: var(--white);
  }
  .hero-photo {
    position: absolute;
    inset: 0;
    background:
      linear-gradient(180deg, rgba(0,0,0,0) 40%, rgba(20,20,24,0.45) 100%),
      linear-gradient(90deg, var(--shade-left) 0%, #4a4542 18%, var(--shade-mid) 45%, #5a4d4a 72%, var(--shade-warm) 100%);
  }
  .brand {
    position: absolute;
    top: 138px;
    left: 0;
    width: 100%;
    text-align: center;
    font-family: "Playfair Display", serif;
    font-weight: 400;
    font-size: 76px;
    line-height: 1;
    letter-spacing: 1px;
  }
  .headline {
    position: absolute;
    top: 278px;
    left: 0;
    width: 100%;
    text-align: center;
    font-family: "Playfair Display", serif;
    font-weight: 400;
    font-size: 52px;
    line-height: 1;
    letter-spacing: 1px;
  }
  .services {
    position: absolute;
    top: 344px;
    left: 0;
    width: 100%;
    text-align: center;
    font-family: "Libre Baskerville", serif;
    font-size: 16px;
    line-height: 1;
    letter-spacing: 0.2px;
  }
  .enter-button {
    position: absolute;
    top: 390px;
    left: 549px;
    width: 103px;
    height: 37px;
    background: var(--accent-red);
    border-radius: 3px;
    display: flex;
    align-items: center;
    justify-content: center;
    font-family: "Open Sans", sans-serif;
    font-weight: 700;
    font-size: 15px;
    color: var(--white);
    text-decoration: none;
  }
  .page-code {
    position: absolute;
    right: 33px;
    bottom: 30px;
    font-family: "Open Sans", sans-serif;
    font-size: 13px;
    color: var(--white);
  }
</style>
</head>
<body>
  <main class="landing">
    <div class="hero-photo" role="img" aria-label="Photo of a young team discussing contracts around a tablet in a brick-walled office, darkened"></div>
    <div class="brand">Pactwise</div>
    <h1 class="headline">CONTRACTS</h1>
    <p class="services">TRAINING I CONSULTING I DESIGN</p>
    <a class="enter-button" href="#">ENTER</a>
    <span class="page-code">M1</span>
  </main>
</body>
</html>
```